3月15日にガールズバーをオープン致しました。
ビルの入り口に置いて使うA1立て看板の製作をお願いします。
A4など縮小サイズでもいただけると助かります。
白を基調とした夜でも目立つ感じにしたいです。

セット料金 40分2000円 tax&service 20%

チャージのみ1時間1500円 tax&service 15

クレジットチャージ 10%
飲み放題付き (焼酎 ウイスキー カクテルなど)
ビル3階 席数17席  団体客歓迎

若いギャル系の女の子の写真を大きく入れて頂きたいのですが素材が無く
困ってます。素材をお持ちかたにお願いしたいと思ってます。

現在の看板を添付致しました。ご参考までに。
文章は記載しないでも大丈夫です。

店舗名 Sunflower(サンフラワー)です。

よろしくお願いします。
資料を再添付致しました。よろしくお願いします。
依頼金額を25000円に変更して、延長しました。
提案下さった皆様ありがとうございます。
もう少し提案を見させていただけたらと思います。

具体的なイメージをデザベース様の過去の事例で近いものを添付致しました。
よろしくお願いします。

最初に思い描いてたイメージより良かったです
女の子と背景のピンクもかわいいくて満足です。

ありがとうございました!

提案くださった皆様ありがとうございます!
修正をしてくださった皆様も早急な対応に感謝致します。

ありがとうございました!

```html
<!DOCTYPE html>
<html lang="ja">
<head>
<meta charset="utf-8">
<title>Sunflower Girl's Bar</title>
<link href="https://fonts.googleapis.com/css2?family=Bodoni+Moda:wght@400;500&family=Noto+Serif+JP:wght@400;500;600&family=Noto+Sans+JP:wght@400;500&display=swap" rel="stylesheet">
<style>
  :root {
    --pink: #ec7b9c;
    --pink-soft: #f4a9bd;
    --pink-light: #fbe3ea;
    --gray-dark: #5b5b5e;
    --gray: #7d7d80;
    --gray-light: #b9b9bc;
    --paper: #ffffff;
    --paper-shade: #f2f1f1;
  }
  * { margin: 0; padding: 0; box-sizing: border-box; }
  html, body { width: 849px; height: 1200px; overflow: hidden; background: var(--paper); }
  .signboard {
    position: relative; width: 849px; height: 1200px; overflow: hidden;
    background: linear-gradient(180deg, var(--paper) 0%, var(--paper) 55%, var(--paper-shade) 100%);
    font-family: "Noto Serif JP", serif; color: var(--gray-dark);
  }
  .photo-area {
    position: absolute; left: 390px; top: 250px; width: 459px; height: 880px;
    background:
      radial-gradient(ellipse at 45% 35%, #f3dccd 0%, rgba(243,220,205,0) 45%),
      radial-gradient(ellipse at 55% 75%, #ece7e3 0%, rgba(236,231,227,0) 60%),
      linear-gradient(180deg, #ffffff 0%, #f6eeea 50%, #efe9e6 100%);
  }
  .tagline {
    position: absolute; left: 72px; top: 28px; font-size: 27px; letter-spacing: 3px; color: var(--gray);
  }
  .tagline .accent { color: var(--pink); }
  .shop-name {
    position: absolute; left: 58px; top: 104px; width: 740px;
    font-family: "Bodoni Moda", serif; font-weight: 400; font-size: 140px; line-height: 1;
    letter-spacing: 0; color: var(--gray-dark); white-space: nowrap;
  }
  .shop-sub {
    position: absolute; left: 490px; top: 300px; font-size: 20px; color: var(--gray);
    font-family: "Bodoni Moda", serif; letter-spacing: 1px;
  }
  .shop-sub span { font-family: "Noto Serif JP", serif; margin-left: 14px; font-size: 18px; }
  .price {
    position: absolute; left: 50px; width: 360px; padding-left: 18px;
    border-left: 6px solid var(--gray-dark);
  }
  .price--set { top: 352px; }
  .price--charge { top: 530px; }
  .price__label { font-size: 26px; color: var(--gray-dark); letter-spacing: 2px; }
  .price__amount {
    margin-top: 6px; font-size: 62px; line-height: 1.1; color: var(--pink); font-weight: 500;
    border-bottom: 2px solid var(--gray-light); padding-bottom: 6px; white-space: nowrap;
  }
  .price__amount small { font-size: 34px; }
  .price__tax {
    margin-top: 10px; font-size: 18px; color: var(--gray); font-family: "Bodoni Moda", serif; letter-spacing: 1px;
  }
  .price__tax span { margin-left: 40px; }
  .credit {
    position: absolute; left: 50px; top: 735px; width: 370px; height: 42px;
    border: 2px solid var(--gray-light); font-size: 19px; color: var(--gray);
    display: flex; align-items: center; padding-left: 22px; letter-spacing: 1px;
  }
  .credit span { margin-left: 24px; }
  .free-drink {
    position: absolute; left: 20px; top: 868px; width: 216px; height: 216px; border-radius: 50%;
    background: var(--pink-soft); border: 6px solid var(--pink-light);
    display: flex; flex-direction: column; align-items: center; justify-content: center; color: #fff;
    text-align: center;
  }
  .free-drink__title { font-size: 38px; line-height: 1.25; font-weight: 600; }
  .free-drink__note { margin-top: 12px; font-size: 12px; line-height: 1.6; }
  .info-band {
    position: absolute; left: 0; top: 1126px; width: 849px; height: 74px;
    display: flex; align-items: center; background: var(--paper);
  }
  .info-band__floor {
    width: 283px; height: 74px; background: var(--gray-dark); color: #fff;
    font-size: 44px; display: flex; align-items: center; justify-content: center; letter-spacing: 2px;
  }
  .info-band__seats { width: 297px; text-align: center; font-size: 38px; color: var(--gray-dark); letter-spacing: 2px; }
  .info-band__group {
    width: 255px; height: 60px; border: 2px solid var(--pink); color: var(--pink);
    font-size: 34px; display: flex; align-items: center; justify-content: center; letter-spacing: 1px;
  }
</style>
</head>
<body>
<main class="signboard">
  <div class="photo-area" role="img" aria-label="白いブラウスの若い女性が両手でグラスを口元に持つ写真"></div>

  <p class="tagline">シックで<span class="accent">かわいい</span>ガールズバー<span class="accent">♡</span></p>
  <h1 class="shop-name">Sunflower</h1>
  <p class="shop-sub">Girl's Bar<span>サンフラワー</span></p>

  <section class="price price--set">
    <p class="price__label">セット料金</p>
    <p class="price__amount">40<small>分</small> 2,000<small>円</small></p>
    <p class="price__tax">Tax &amp; Service<span>20%</span></p>
  </section>

  <section class="price price--charge">
    <p class="price__label">チャージのみ</p>
    <p class="price__amount">60<small>分</small> 1,500<small>円</small></p>
    <p class="price__tax">Tax &amp; Service<span>15%</span></p>
  </section>

  <p class="credit">クレジットチャージ<span>10%</span></p>

  <div class="free-drink">
    <p class="free-drink__title">飲み放題<br>付き♡</p>
    <p class="free-drink__note">焼酎・ウイスキー・カクテル<br>など</p>
  </div>

  <footer class="info-band">
    <p class="info-band__floor">当ビル3階</p>
    <p class="info-band__seats">席数17席</p>
    <p class="info-band__group">団体客様♡歓迎</p>
  </footer>
</main>
</body>
</html>
```